New business card design for Pinecrest Hollow Optometry Clinic

We need a new business card design using our existing logo (uploaded). Please do not include eyes, eye exam charts or beaches, water, sand. The logo I uploaded shows our colors of green and blue, but we are open to seeing it in black OR white. We would like to see something modern and fresh. It will need to be 2 sided. On the front we will need to be able to put a doctors name, for example-Dr Marta Kellerman and Associates. We will need to be able to change the name to other doctors names when we send for printing. The back of the card should list the following: 3817 Tarrow St, Larkmere Bay (P)705-555-0148 (E) info@phoc.ca www.phoc.ca. "We are welcoming new patients" and a line for the appointment date and time. I have uploaded the back of a card to give an example

```html
<!DOCTYPE html>
<html lang="en">
<head>
<meta charset="utf-8">
<title>Pinecrest Hollow Optometry Clinic – Business Card</title>
<link href="https://fonts.googleapis.com/css2?family=Montserrat:ital,wght@0,400;0,500;0,700;1,400&display=swap" rel="stylesheet">
<style>
  :root {
    --bg: #cdd9e5;
    --paper: #ffffff;
    --paper-back: #fbfbfb;
    --brand-blue: #3b52a3;
    --brand-teal: #287a78;
    --brand-green: #1b9b4b;
    --lavender: #7c86c6;
    --soft-green: #6fae73;
    --text-blue: #3d55a5;
    --text-green: #3f9447;
    --rule: #b5b5b5;
    --label: #777777;
    --icon: #111111;
  }
  * { margin: 0; padding: 0; box-sizing: border-box; }
  html, body {
    width: 1200px; height: 710px; overflow: hidden;
    background: var(--bg);
    font-family: "Montserrat", Arial, sans-serif;
  }
  .canvas { position: relative; width: 1200px; height: 710px; }
  .card-slot {
    position: absolute; top: 193px;
    width: 560px; height: 323.4px;
  }
  .card-slot--front { left: 25px; }
  .card-slot--back { left: 615px; }
  .card {
    position: absolute; top: 0; left: 0;
    width: 800px; height: 462px;
    transform: scale(0.7); transform-origin: top left;
    overflow: hidden;
    box-shadow: 0 10px 22px rgba(60, 110, 160, 0.35);
  }
  .card--front { background: var(--paper); }
  .card--back { background: var(--paper-back); }

  /* Front */
  .front-art {
    position: absolute; left: 0; top: 0; width: 800px; height: 380px;
    background:
      linear-gradient(to bottom, rgba(255,255,255,0.55) 0%, rgba(255,255,255,0) 14%, rgba(255,255,255,0) 62%, #ffffff 100%),
      linear-gradient(to right, var(--brand-blue) 0%, var(--brand-teal) 48%, var(--brand-green) 100%);
  }
  .clinic-name {
    position: absolute; left: 200px; top: 160px; width: 400px;
    text-align: center;
    color: #ffffff;
    font-weight: 700; font-size: 30px; line-height: 1.2;
  }
  .doctor-name {
    position: absolute; left: 0; right: 0; top: 393px;
    text-align: center;
    color: var(--text-blue);
    font-weight: 500; font-size: 25px; letter-spacing: 3px;
  }

  /* Back */
  .back-art {
    position: absolute; left: 0; bottom: 0; width: 800px; height: 90px;
    background:
      linear-gradient(to bottom, var(--paper-back) 0%, rgba(251,251,251,0) 60%),
      linear-gradient(to right, var(--lavender) 0%, var(--soft-green) 45%, var(--lavender) 75%, var(--soft-green) 100%);
  }
  .contact-list {
    position: absolute; left: 46px; top: 146px;
    list-style: none;
  }
  .contact-item {
    display: flex; align-items: center;
    height: 35px;
    color: var(--text-green);
    font-size: 17px; letter-spacing: 0.3px;
    white-space: nowrap;
  }
  .contact-icon { width: 24px; height: 20px; margin-right: 16px; fill: var(--icon); flex: none; }
  .divider {
    position: absolute; left: 399px; top: 108px;
    width: 2px; height: 212px; background: var(--text-blue);
  }
  .appointment { position: absolute; left: 452px; top: 150px; width: 290px; }
  .appointment-title {
    color: var(--text-blue); font-size: 15.5px; font-weight: 500;
    white-space: nowrap;
  }
  .fill-line { margin-top: 36px; border-top: 1px solid var(--rule); }
  .fill-line + .fill-line { margin-top: 40px; }
  .fill-label {
    display: block; padding-top: 4px;
    color: var(--label); font-size: 11.5px; font-style: italic;
  }
</style>
</head>
<body>
<main class="canvas">

  <div class="card-slot card-slot--front">
    <section class="card card--front" aria-label="Card front">
      <div class="front-art" role="img" aria-label="Soft blue-to-green flowing background art"></div>
      <p class="clinic-name">Pinecrest Hollow Optometry Clinic</p>
      <h1 class="doctor-name">Dr Marta Kellerman</h1>
    </section>
  </div>

  <div class="card-slot card-slot--back">
    <section class="card card--back" aria-label="Card back">
      <div class="back-art" role="img" aria-label="Soft lavender and green background band"></div>

      <ul class="contact-list">
        <li class="contact-item">
          <svg class="contact-icon" viewBox="0 0 24 24" aria-hidden="true"><path d="M12 1C7.6 1 5 4.2 5 8c0 5 7 14 7 14s7-9 7-14c0-3.8-2.6-7-7-7zm0 10a3 3 0 1 1 0-6 3 3 0 0 1 0 6z"/></svg>
          <span>3817 Tarrow St, Larkmere Bay</span>
        </li>
        <li class="contact-item">
          <svg class="contact-icon" viewBox="0 0 24 24" aria-hidden="true"><path d="M2 8c0-2 4-4 10-4s10 2 10 4v2h-5V8c-1-.6-3-1-5-1s-4 .4-5 1v2H2zM6 12l2-3h8l2 3v7H6zm6 1.5a2 2 0 1 0 0 4 2 2 0 0 0 0-4z"/></svg>
          <span>705-555-0148</span>
        </li>
        <li class="contact-item">
          <svg class="contact-icon" viewBox="0 0 24 24" aria-hidden="true"><path d="M2 5h20v14H2zm2 2v.5l8 6 8-6V7zm0 3v7h16v-7l-8 6z"/></svg>
          <span>info@phoc.ca</span>
        </li>
        <li class="contact-item">
          <svg class="contact-icon" viewBox="0 0 24 24" aria-hidden="true"><path d="M12 2a10 10 0 1 0 0 20 10 10 0 0 0 0-20zm-1 2.1V8H7.6C8.4 5.8 9.6 4.4 11 4.1zm2 0c1.4.3 2.6 1.7 3.4 3.9H13zM5.3 10H11v3H4.9a8 8 0 0 1 .4-3zm7.7 0h5.7a8 8 0 0 1 .4 3H13zm-8.1 5H11v4.9c-1.4-.3-2.6-2.2-3.2-4.9zm8.1 0h3.2c-.6 2.7-1.8 4.6-3.2 4.9z"/></svg>
          <span>www.phoc.ca.</span>
        </li>
      </ul>

      <div class="divider"></div>

      <div class="appointment">
        <p class="appointment-title">We are welcoming new patients!</p>
        <div class="fill-line"><span class="fill-label">Appointment Date</span></div>
        <div class="fill-line"><span class="fill-label">Time</span></div>
      </div>
    </section>
  </div>

</main>
</body>
</html>
```